Automotive component supplier needs a business card design

We need a business card design for our company called Velmar Global Components Ltd based in the UK. We are a supplier of interior and exterior components to premium car manufacturers such as Corvane Hale, Durrant Fyfe, Maxtorn and Valdessimo. We would like to see a modern business card design that uses the colour blue.

Target Market(s)

Premium automotive car manufacturers.

Industry/Entity Type

Automotive

Contact Information for Business Card

Company Name : Velmar Global Components Limited
Address: 17 Tamsey Yard, Upper Drisk, Warwick, CV31 8RJ, United Kingdom
Web Address : www.velmarparts-example.co.uk

Font styles to use
Other font styles liked:
• Helvetica

Colors
3176b5
0255a3
85acd3
cfdeed
cee9f5
85cae6
34a6d7
0692cd
9bcb3c

Requirements
Must have
• Clear company logo and a mixture of blue colours.
Nice to have
• A high quality modern image.
Should not have
• Multiple colours.

```html
<!DOCTYPE html>
<html lang="en">
<head>
<meta charset="utf-8">
<title>Velmar Global Components – Business Card</title>
<link href="https://fonts.googleapis.com/css2?family=Open+Sans:wght@400;700&display=swap" rel="stylesheet">
<style>
  :root {
    --bg: #eceae6;
    --card-blue: #3a8ec9;
    --brand-blue: #0692cd;
    --ink: #1a1a1a;
    --white: #ffffff;
    --soft-white: #e6f0f8;
  }
  * { box-sizing: border-box; margin: 0; padding: 0; }
  html, body {
    width: 1200px; height: 801px; overflow: hidden;
    background: var(--bg);
    font-family: "Open Sans", Arial, sans-serif;
  }
  .sheet {
    position: relative; width: 1200px; height: 801px;
    display: flex; align-items: center; justify-content: center; gap: 40px;
  }
  .card {
    width: 540px; height: 310px; position: relative;
    box-shadow: 0 4px 14px rgba(0,0,0,0.12);
  }
  /* Front */
  .card--front { background: var(--white); }
  .brand {
    position: absolute; left: 40px; top: 128px; width: 220px;
    color: var(--brand-blue); font-weight: 700;
  }
  .brand__name { font-size: 44px; line-height: 1; letter-spacing: 3px; }
  .brand__sub { font-size: 12.5px; letter-spacing: 2px; margin-top: 6px; }
  .divider {
    position: absolute; left: 272px; top: 80px; width: 2px; height: 150px;
    background: var(--ink);
  }
  .contact {
    position: absolute; left: 292px; top: 84px; list-style: none;
    font-size: 13px; line-height: 1.3; color: var(--ink);
  }
  .contact li { display: flex; align-items: flex-start; gap: 8px; margin-bottom: 6px; }
  .contact svg { flex: 0 0 12px; width: 12px; height: 12px; margin-top: 2px; fill: var(--brand-blue); }
  /* Back */
  .card--back {
    background: var(--card-blue); color: var(--white);
    display: flex; flex-direction: column; align-items: center; justify-content: center;
  }
  .back-name { font-weight: 700; font-size: 52px; letter-spacing: 4px; line-height: 1; }
  .back-sub { font-weight: 700; font-size: 15px; letter-spacing: 3px; margin-top: 8px; }
  .back-url { font-size: 11px; letter-spacing: 1px; margin-top: 34px; color: var(--soft-white); text-transform: uppercase; }
</style>
</head>
<body>
<main class="sheet">
  <section class="card card--front">
    <div class="brand">
      <div class="brand__name">VELMAR</div>
      <div class="brand__sub">GLOBAL COMPONENTS</div>
    </div>
    <div class="divider"></div>
    <ul class="contact">
      <li>
        <svg viewBox="0 0 12 12"><path d="M6 0a4 4 0 0 0-4 4c0 3 4 8 4 8s4-5 4-8a4 4 0 0 0-4-4zm0 5.5A1.5 1.5 0 1 1 6 2.5a1.5 1.5 0 0 1 0 3z"/></svg>
        <span>17 Tamsey Yard, Upper Drisk,<br>Warwick, CV31 8RJ, United Kingdom</span>
      </li>
      <li>
        <svg viewBox="0 0 12 12"><path d="M1 4c0-1.5 2-2.5 5-2.5S11 2.5 11 4v1H8.5V4h-5v1H1zM2 6h8l1 5H1z"/></svg>
        <span>000 000 0000</span>
      </li>
      <li>
        <svg viewBox="0 0 12 12"><path d="M3.5 0h5a1 1 0 0 1 1 1v10a1 1 0 0 1-1 1h-5a1 1 0 0 1-1-1V1a1 1 0 0 1 1-1zm.5 1.5v8h4v-8z"/></svg>
        <span>000 000 0000</span>
      </li>
      <li>
        <svg viewBox="0 0 12 12"><path d="M0 2.5h12v7H0zM1 3.3 6 7l5-3.7v-.3H1z"/></svg>
        <span>hello@velmarparts-example.co.uk</span>
      </li>
      <li>
        <svg viewBox="0 0 12 12"><path d="M6 0a6 6 0 1 0 0 12A6 6 0 0 0 6 0zm0 1c.7 0 1.4 1.6 1.6 4H4.4C4.6 2.6 5.3 1 6 1zM4.4 6h3.2C7.4 8.4 6.7 11 6 11S4.6 8.4 4.4 6zM1 5a5 5 0 0 1 2.5-3.4C3.2 2.6 3.5 3.8 3.4 5zm0 1h2.4c0 1.2.2 2.4.6 3.4A5 5 0 0 1 1 6zm7.6-1c0-1.2-.3-2.4-.6-3.4A5 5 0 0 1 11 5zm0 1H11a5 5 0 0 1-3 3.4c.4-1 .6-2.2.6-3.4z"/></svg>
        <span>www.velmarparts-example.co.uk</span>
      </li>
    </ul>
  </section>

  <section class="card card--back">
    <div class="back-name">VELMAR</div>
    <div class="back-sub">GLOBAL COMPONENTS</div>
    <div class="back-url">www.velmarparts-example.co.uk</div>
  </section>
</main>
</body>
</html>
```